House-share and Room Rental Website (With Focus on the Bedroom Landing Page)

Looking for website design for our House-share (executive accommodation) and room rental business.

Our company name is: Quellnest could also be written as QuellNest or quellnest. Either is fine .. just looking for a nice clean catchy logo to go with the design.

EXAMPLES
These are examples of other websites in this field that are doing well. this is a kind of baseline.
https://dovelinter.example.au/
https://www.kestrib.example/
https://www.velunor.example/
https://www.trisbel.example/
https://www.pondmarrowseek.example.au/

Our business model is to rent rooms to people looking for high-quality accommodation. We fill the gap between those looking to rent rooms and those with rooms to rent. However, our model is slightly different from those already on the market as we looking to fill a massive gap in the market delivering upmarket rooms for rent.(Executive Accommodation) also in the back end will be coupled with a self management process in the back end.

We offer executive style accommodation that stands out above the rest. With special extras like fire safety.. and management processes that create happier homes. We are looking for a web design package that can help us grow and scale our business. We need a design that is captivating

Our MAIN focus is having a room landing page that stands out from the rest... The core of our business will rely on the promotion of the rooms in a share house... so the whole design relies on the BEDROOM landing page to drive results.

Target Market(s)

We have 2 markets we are aiming at ... the first market is people offering rooms to rent who want the highest rental return. The second market is people looking to rent safe, high-quality rooms, in houses that are well managed and looked after.

Industry/Entity Type

Share Economy

Logo Text

QuellNest

Number of Pages Required

5+ page

Font styles to use
Sans Serif

Colors
3276b5

Requirements
Must have
• A messaging system whereby we can create direct communication between those offering rooms and those looking for rooms.
• A call to action that says " Schedule an Inspection"
• Landing page for promoting rooms
• A home page for showing stock.
• Profile page for those selling rooms
• Profile page for those looking for rooms.
• A scheduling calendar for booking inspections
Nice to have
• Pages where new residents can lock in a room.. pay bond and rents.. and sign contracts
• Notifications
• SMS capabilities in the backend.
Should not have
• No script or handwriting fonts.

```html
<!DOCTYPE html>
<html lang="en">
<head>
<meta charset="utf-8">
<title>Roomvale – Rental Rooms</title>
<link rel="stylesheet" href="https://fonts.googleapis.com/css2?family=Questrial&family=Open+Sans:wght@400;600&display=swap">
<style>
  :root {
    --brand: #3276b5;
    --brand-dark: #2a64a0;
    --navy: #1c3a63;
    --ink: #333333;
    --muted: #555555;
    --field: #ececec;
    --hero-bg: #eef0f3;
    --white: #ffffff;
  }
  * { box-sizing: border-box; margin: 0; padding: 0; }
  html, body { width: 714px; height: 1200px; overflow: hidden; background: var(--white); }
  body { position: relative; font-family: "Questrial", sans-serif; color: var(--ink); }

  .abs { position: absolute; }

  /* Hero */
  .hero { left: 0; top: 0; width: 714px; height: 448px; }
  .hero-bg { position: absolute; inset: 0; }
  .logo { left: 47px; top: 14px; font-size: 22px; color: var(--brand); }
  .btn-signup, .btn-login {
    top: 15px; height: 26px; border-radius: 8px; font-size: 13px;
    display: flex; align-items: center; justify-content: center;
  }
  .btn-signup { left: 538px; width: 73px; background: var(--brand); color: var(--white); }
  .btn-login { left: 615px; width: 73px; border: 2px solid var(--brand); color: var(--brand); background: var(--white); }
  .hero-title { left: 36px; top: 128px; font-size: 25px; line-height: 30px; color: var(--brand); font-weight: 400; }
  .hero-text { left: 36px; top: 189px; width: 280px; font-family: "Open Sans", sans-serif; font-size: 9.6px; line-height: 22.5px; color: var(--ink); font-weight: 600; }
  .btn-cta {
    left: 38px; top: 275px; width: 205px; height: 37px; border-radius: 7px;
    background: var(--brand); color: var(--white); font-size: 15px;
    display: flex; align-items: center; justify-content: center;
  }
  .hero-photo { left: 330px; top: 134px; width: 321px; height: 160px; border: 2px solid var(--brand);
    background: linear-gradient(100deg, #2c2c2c 0%, #4a4a4a 45%, #7a7670 75%, #c9b79a 100%); }

  /* Rooms */
  .section-title { left: 0; top: 466px; width: 714px; text-align: center; font-size: 27px; color: var(--brand); font-weight: 400; }

  .room-card { width: 185px; background: var(--white); box-shadow: 0 0 6px rgba(0,0,0,0.14); }
  .room-photo { position: absolute; left: 9px; top: 8px; width: 167px; height: 102px; }
  .room-name { position: absolute; left: 0; width: 100%; text-align: center; font-size: 12.5px; color: var(--brand); }
  .room-desc { position: absolute; left: 15px; width: 157px; font-family: "Open Sans", sans-serif; font-size: 6.4px; line-height: 10px; color: var(--muted); }
  .room-foot { position: absolute; left: 3px; right: 3px; height: 1px; background: var(--brand); }
  .room-price { position: absolute; left: 9px; font-size: 12px; color: var(--brand); }
  .room-share { position: absolute; left: 62px; width: 54px; height: 14px; background: var(--brand); color: var(--white);
    font-family: "Open Sans", sans-serif; font-size: 6.5px; display: flex; align-items: center; justify-content: center; }
  .room-like { position: absolute; right: 9px; width: 14px; height: 12px; }

  .filter-card { left: 275px; top: 510px; width: 181px; height: 192px; background: var(--white); box-shadow: 0 0 6px rgba(0,0,0,0.14); }
  .filter-title { position: absolute; left: 0; top: 8px; width: 100%; text-align: center; font-size: 9.5px; color: var(--brand); }
  .filter-field { position: absolute; left: 28px; width: 135px; height: 18px; border-radius: 9px; background: var(--field);
    font-family: "Open Sans", sans-serif; font-size: 9px; color: #777; padding-left: 11px; display: flex; align-items: center; }
  .filter-submit { position: absolute; left: 85px; top: 155px; width: 78px; height: 20px; border-radius: 7px; background: var(--brand);
    color: var(--white); font-size: 10px; display: flex; align-items: center; justify-content: center; }

  /* Features */
  .feature-title { font-size: 22px; line-height: 26px; color: var(--brand); font-weight: 400; }
  .feature-text { font-family: "Open Sans", sans-serif; font-size: 9.6px; line-height: 17.5px; color: var(--muted); width: 190px; }
  .btn-enquire { width: 166px; height: 30px; border-radius: 7px; background: var(--brand); color: var(--white); font-size: 13px;
    display: flex; align-items: center; justify-content: center; }

  /* Footer */
  .footer-shape { left: 0; top: 986px; width: 714px; height: 196px; }
  .footer-heading { font-size: 16px; color: var(--white); }
  .footer-list { font-size: 12px; line-height: 17.5px; color: var(--white); list-style: none; }
  .legal-bar { left: 0; top: 1180px; width: 714px; height: 20px; background: var(--navy); color: var(--white);
    font-family: "Open Sans", sans-serif; font-size: 9px; }
  .legal-bar .copy { position: absolute; left: 12px; top: 4px; }
  .legal-bar .links { position: absolute; right: 9px; top: 5px; }
</style>
</head>
<body>

  <header class="abs hero">
    <svg class="hero-bg" width="714" height="448" viewBox="0 0 714 448" aria-hidden="true">
      <defs>
        <linearGradient id="heroFade" x1="0" y1="0" x2="0" y2="1">
          <stop offset="0" stop-color="#f4f5f7"/>
          <stop offset="1" stop-color="#e6e9ee"/>
        </linearGradient>
      </defs>
      <path d="M0 0 H714 V392 L357 440 L0 392 Z" fill="url(#heroFade)" role="img" aria-label="Soft faded photo of a bright bedroom behind the header"/>
      <path d="M0 392 L357 440 L714 392 L700 396 L357 448 L14 396 Z" fill="var(--brand)"/>
    </svg>

    <div class="abs logo">Roomvale.com</div>
    <div class="abs btn-signup">Sign Up</div>
    <div class="abs btn-login">Login</div>

    <h1 class="abs hero-title">Easily Get A Rental<br>Room Without&nbsp; Hustle</h1>
    <p class="abs hero-text">Looking for website design for our Houseshare and room rental business. Our business model is to rent rooms to people looking for high quality accommodation.</p>
    <div class="abs btn-cta">Schedule an Inspection</div>

    <div class="abs hero-photo" role="img" aria-label="Photo of a modern concrete-walled bedroom with sunlight through tall windows"></div>

    <svg class="abs" style="left:664px;top:170px" width="42" height="88" viewBox="0 0 42 88" aria-label="Slider arrows" role="img">
      <path d="M38 2 L4 30 L38 50" fill="none" stroke="#333" stroke-width="2"/>
      <path d="M4 40 L38 60 L4 86" fill="none" stroke="var(--brand)" stroke-width="2"/>
    </svg>
  </header>

  <main>
    <h2 class="abs section-title">Available Rooms</h2>

    <article class="abs room-card" style="left:46px;top:518px;height:203px">
      <div class="room-photo" role="img" aria-label="Photo of a bedroom with a patterned bedspread and a book" style="background:linear-gradient(180deg,#d9c4c6 0%,#b9a8b0 55%,#8d8fa3 100%)"></div>
      <div class="room-name" style="top:117px">One Bedroom</div>
      <p class="room-desc" style="top:134px">"Lorem ipsum dolor sit amet, consectetur adipiscing elit, sed do eiusmod tempor incididunt ut labore et dolore magna aliqua. Ut enim ad</p>
      <div class="room-foot" style="top:174px"></div>
      <div class="room-price" style="top:182px">$ 5000</div>
      <div class="room-share" style="top:181px">Share Room</div>
      <svg class="room-like" style="top:184px" viewBox="0 0 14 12" aria-hidden="true"><path d="M7 12 L1 6 A3.2 3.2 0 0 1 7 2 A3.2 3.2 0 0 1 13 6 Z" fill="var(--brand)"/></svg>
    </article>

    <form class="abs filter-card">
      <div class="filter-title">FILTER FROM OUR DATABASE</div>
      <div class="filter-field" style="top:27px">Address</div>
      <div class="filter-field" style="top:56px">Rental Price</div>
      <div class="filter-field" style="top:85px">Location</div>
      <div class="filter-field" style="top:115px">Furnished</div>
      <div class="filter-submit">Submit</div>
    </form>

    <article class="abs room-card" style="left:498px;top:506px;height:211px">
      <div class="room-photo" role="img" aria-label="Photo of striped pillows on a white bed" style="top:9px;height:106px;background:linear-gradient(135deg,#f3efe9 0%,#d8cfc4 50%,#7e7468 100%)"></div>
      <div class="room-name" style="top:120px">One Bedroom</div>
      <p class="room-desc" style="top:136px">"Lorem ipsum dolor sit amet, consectetur adipiscing elit, sed do eiusmod tempor incididunt ut labore et dolore magna aliqua. Ut enim ad</p>
      <div class="room-foot" style="top:177px"></div>
      <div class="room-price" style="top:185px">$ 5000</div>
      <div class="room-share" style="left:69px;top:187px">Share Room</div>
      <svg class="room-like" style="top:186px" viewBox="0 0 14 12" aria-hidden="true"><path d="M7 12 L1 6 A3.2 3.2 0 0 1 7 2 A3.2 3.2 0 0 1 13 6 Z" fill="var(--brand)"/></svg>
    </article>

    <section>
      <h3 class="abs feature-title" style="left:21px;top:766px">Get A Room Worth<br>Your Money</h3>
      <p class="abs feature-text" style="left:21px;top:830px">"Lorem ipsum dolor sit amet, consectetur adipiscing elit, sed do eiusmod tempor incididunt ut labore et dolore magna aliqua. Ut enim ad minim veniam, quis</p>
      <div class="abs btn-enquire" style="left:22px;top:910px">Enquire How</div>

      <article class="abs room-card" style="left:228px;top:760px;height:203px">
        <div class="room-photo" role="img" aria-label="Photo of a bed in a concrete-walled room beside tall windows" style="left:6px;width:171px;background:linear-gradient(100deg,#2c2c2c 0%,#4c4c4c 50%,#8a8378 80%,#c9b79a 100%)"></div>
        <div class="room-name" style="top:116px">One Bedroom</div>
        <p class="room-desc" style="top:133px">"Lorem ipsum dolor sit amet, consectetur adipiscing elit, sed do eiusmod tempor incididunt ut labore et dolore magna aliqua. Ut enim ad</p>
        <div class="room-foot" style="top:173px"></div>
        <div class="room-price" style="top:181px">$ 5000</div>
        <div class="room-share" style="left:77px;top:183px">Share Room</div>
        <svg class="room-like" style="top:183px" viewBox="0 0 14 12" aria-hidden="true"><path d="M7 12 L1 6 A3.2 3.2 0 0 1 7 2 A3.2 3.2 0 0 1 13 6 Z" fill="var(--brand)"/></svg>
      </article>

      <h3 class="abs feature-title" style="left:464px;top:774px">It’s as easy and straight<br>forward</h3>
      <p class="abs feature-text" style="left:464px;top:832px">"Lorem ipsum dolor sit amet, consectetur adipiscing elit, sed do eiusmod tempor incididunt ut labore et dolore magna aliqua. Ut enim ad minim veniam, quis</p>
      <div class="abs btn-enquire" style="left:465px;top:914px">Enquire How</div>
    </section>
  </main>

  <footer>
    <svg class="abs footer-shape" viewBox="0 0 714 196" aria-hidden="true">
      <path d="M0 0 L357 42 L714 0 V196 H0 Z" fill="var(--brand)"/>
    </svg>
    <h4 class="abs footer-heading" style="left:11px;top:1054px">CONTACT US</h4>
    <ul class="abs footer-list" style="left:13px;top:1079px">
      <li>Alder Street 1234</li>
      <li>NY, Example</li>
      <li>infor@roomvale.com</li>
      <li>www.roomvale.com</li>
    </ul>
    <h4 class="abs footer-heading" style="left:593px;top:1054px">QUICK LINKS</h4>
    <ul class="abs footer-list" style="left:594px;top:1079px">
      <li>Bedrooms</li>
      <li>Sitting Rooms</li>
      <li>Homes</li>
    </ul>
    <div class="abs legal-bar">
      <span class="copy">© Roomvale Ltd 2019</span>
      <span class="links">Terms | Privacy Policy</span>
    </div>
  </footer>

</body>
</html>
```